Apply styling to powerpoint presentation

Apply the styling of the attached flyer (which you designed) to a power point presentation I will send (about 100 slides). You will need to manually add some text as it part of images. Use the same primary background colour, the white text for body, and white text with the orange container for headers. Please do not include the Velmora logo at all.
Please include master slides.

```html
<!DOCTYPE html>
<html lang="en">
<head>
<meta charset="utf-8">
<title>Presentation Template Overview</title>
<link href="https://fonts.googleapis.com/css2?family=Lato:wght@400;700;900&family=Open+Sans:wght@400;600;700&display=swap" rel="stylesheet">
<style>
  :root{
    --orange:#f58220;
    --blue:#1a6aa6;
    --blue-deep:#135a8f;
    --blue-dark:#144a75;
    --blue-light:#2a86c8;
    --navy-text:#165a8c;
    --stage:#dcdcdc;
    --white:#ffffff;
    --head:'Lato',sans-serif;
    --body:'Open Sans',sans-serif;
  }
  *{margin:0;padding:0;box-sizing:border-box}
  html,body{width:1200px;height:956px;overflow:hidden}
  body{position:relative;background:var(--stage);font-family:var(--body);color:var(--white)}
  .stage-band{position:absolute;inset:0}
  .slide{position:absolute;width:339px;height:191px;overflow:hidden;
    background:linear-gradient(165deg,var(--blue-deep) 0%,var(--blue) 55%,#1c74b4 100%);
    box-shadow:0 7px 14px rgba(0,0,0,.28)}
  .c1{left:72px}.c2{left:430px}.c3{left:788px}
  .r1{top:75px}.r2{top:283px}.r3{top:491px}.r4{top:700px}
  .abs{position:absolute}
  .header-bar{position:absolute;left:0;top:17px;width:321px;height:19px;background:var(--orange);
    font:700 13px/19px var(--head);padding-left:21px;color:var(--white);white-space:nowrap}
  .page-no{position:absolute;right:14px;bottom:3px;font:700 11px var(--head);color:#2e8fd3}
  .page-no.tiny{font-size:4px;color:#7fb3da;right:26px;bottom:8px}
  .presenter-tag{background:var(--orange);font:600 5.6px/15px var(--body);letter-spacing:1.6px;text-transform:uppercase}
  .copy{font-size:5.1px;line-height:1.3;text-align:justify}
  .copy p+p{margin-top:5px}
  .illustration{position:absolute;background:radial-gradient(ellipse at 55% 45%,rgba(150,200,240,.35),rgba(150,200,240,0) 70%)}

  /* title slide */
  .title-dark{font:700 20px var(--head);color:var(--navy-text);text-align:right}
  .sub-dark{font:400 6px var(--body);letter-spacing:2.2px;color:var(--navy-text);text-align:right}
  .title-light{font:700 20px var(--head);color:var(--white)}
  .sub-light{font:400 6px var(--body);letter-spacing:2.2px;color:#cfe3f3}

  /* welcome */
  .welcome{background:var(--white)}
  .welcome .side{left:0;top:0;width:77px;height:191px;background:var(--blue-dark)}
  .photo-frame{left:36px;top:32px;width:94px;height:126px;background:var(--white);box-shadow:0 2px 6px rgba(0,0,0,.25)}
  .photo{left:5px;top:6px;width:86px;height:114px;background:linear-gradient(160deg,#8a7a6e,#3a3a3c 60%,#1d1d20)}
  .welcome h2{left:143px;top:19px;font:700 17px var(--head);color:var(--orange)}
  .quote-mark{left:139px;top:40px;font:700 34px/1 Georgia,serif;color:#c9c9c9}
  .welcome .copy{color:#4a4a4a;font-size:4.3px;width:166px;left:148px}

  /* section */
  .section-label{left:0;width:172px;text-align:center}

  /* table */
  .data-table{position:absolute;left:21px;top:54px;width:299px;border-collapse:separate;border-spacing:0;font:600 6.4px var(--body)}
  .data-table th{height:17px;text-align:left;padding-left:9px;font:700 7px var(--head);color:var(--white);background:var(--orange);border-left:3px solid transparent;background-clip:padding-box}
  .data-table th:first-child{border-left:0}
  .data-table th.alt{background-color:var(--blue-light)}
  .data-table td{height:16.5px;padding-left:9px;color:var(--white)}
  .data-table tr.light td{background:#f2f2f2;color:#222}

  /* vision */
  .vision-sky{left:0;top:0;width:339px;height:113px;background:linear-gradient(180deg,#d9dde2 0%,#f4f5f7 55%,#e9ebee 100%)}
  .vision-base{left:0;top:113px;width:339px;height:78px;background:var(--blue-dark)}
  .value-card{position:absolute;top:76px;width:81px;height:95px;border-radius:9px;
    background:linear-gradient(180deg,#1f78b8,#1765a0);text-align:center;padding-top:9px}
  .value-card h3{font:600 7.4px var(--head);margin-top:5px;letter-spacing:.3px}
  .value-card p{font-size:3.9px;line-height:1.3;padding:0 7px;margin-top:6px}

  /* timeline */
  .milestone{font:700 10px var(--head)}
  .note{position:absolute;width:56px;text-align:center;font-size:3.7px;line-height:1.25}
  .note b{display:block;font-size:4px;margin-bottom:2px}

  /* six points */
  .point{position:absolute;width:141px;height:25px;border-bottom:.6px solid rgba(255,255,255,.8)}
  .point .num{position:absolute;left:0;top:0;font:700 7px var(--head)}
  .point h4{position:absolute;left:15px;top:.5px;font:600 5.6px var(--body);text-transform:uppercase;white-space:nowrap}
  .point p{position:absolute;left:15px;top:9px;font-size:3.4px;line-height:1.35;width:126px}

  /* cycle */
  .chip{position:absolute;width:66px;height:19px;background:#236fab;font:400 4.8px/19px var(--body);padding-left:23px}
  .chip i{position:absolute;left:0;top:0;width:18px;height:19px;background:#175a8e;display:flex;align-items:center;justify-content:center}

  /* statistics */
  .stat{font:700 13px var(--head);color:var(--orange)}
</style>
</head>
<body>

<svg class="stage-band" width="1200" height="956" aria-hidden="true">
  <polygon points="100,0 1200,0 1200,956 1105,956" fill="var(--orange)"/>
</svg>

<!-- 1 Title -->
<section class="slide c1 r1">
  <svg class="abs" width="339" height="191" style="left:0;top:0" aria-hidden="true">
    <path d="M0,0 L22,0 Q115,150 339,119 L339,130 Q95,172 0,12 Z" fill="#124d78"/>
    <path d="M38,0 Q132,122 339,112 L339,0 Z" fill="#fff"/>
    <path d="M36,0 Q130,124 339,114" fill="none" stroke="var(--orange)" stroke-width="3"/>
    <path d="M62,0 Q150,104 339,101" fill="none" stroke="var(--orange)" stroke-width=".5"/>
  </svg>
  <div class="abs title-dark" style="right:24px;top:38px">Presentation Title</div>
  <div class="abs sub-dark" style="right:24px;top:64px">SUB TITLE GOES HERE</div>
  <div class="abs presenter-tag" style="left:0;top:143px;width:131px;height:16px;padding-left:25px">Name of presenter</div>
  <span class="page-no tiny">1</span>
</section>

<!-- 2 Title alt -->
<section class="slide c2 r1">
  <div class="illustration" role="img" aria-label="Faint anatomical heart illustration" style="left:250px;top:55px;width:95px;height:140px"></div>
  <div class="abs presenter-tag" style="left:208px;top:17px;width:131px;height:15px;text-align:center">Name of presenter</div>
  <div class="abs title-light" style="left:20px;top:83px">Presentation Title</div>
  <div class="abs sub-light" style="left:21px;top:111px">SUB TITLE GOES HERE</div>
  <span class="page-no tiny">2</span>
</section>

<!-- 3 Welcome -->
<section class="slide c3 r1 welcome">
  <div class="abs side"></div>
  <div class="abs photo-frame">
    <div class="abs photo" role="img" aria-label="Portrait photo of the speaker"></div>
  </div>
  <h2 class="abs">Welcome Message</h2>
  <div class="abs quote-mark">“</div>
  <p class="abs copy" style="top:61px;text-align:center">Lorem ipsum dolor sit amet, consectetur adipiscing elit, sed do eiusmod tempor incididunt ut labore et dolore magna aliqua. Lorem ipsum dolor sit amet, consectetur adipiscing elit, sed do eiusmod tempor incididunt ut labore et dolore magna aliqua.</p>
  <p class="abs copy" style="top:100px">Lorem ipsum dolor sit amet, consectetur adipiscing elit, sed do eiusmod tempor incididunt ut labore et dolore magna aliqua. Lorem ipsum dolor sit amet, consectetur adipiscing elit, sed do eiusmod tempor incididunt ut labore et dolore magna aliqua. Lorem ipsum dolor sit amet, consectetur adipiscing elit, sed do eiusmod tempor incididunt ut labore et dolore magna aliqua. Lorem ipsum dolor sit amet, consectetur adipiscing elit, sed do eiusmod tempor incididunt ut labore et dolore magna aliqua.</p>
  <span class="page-no tiny" style="color:#999">3</span>
</section>

<!-- 4 Section break -->
<section class="slide c1 r2">
  <div class="illustration" role="img" aria-label="Faint anatomical heart illustration" style="left:215px;top:10px;width:130px;height:185px"></div>
  <svg class="abs" width="26" height="24" viewBox="0 0 26 24" style="left:159px;top:62px" aria-hidden="true">
    <rect x="1.5" y="4.5" width="18" height="18" rx="3" fill="none" stroke="#fff" stroke-width="2.5"/>
    <path d="M6,12 L11,17 L24,3" fill="none" stroke="#fff" stroke-width="3.2" stroke-linecap="round" stroke-linejoin="round"/>
  </svg>
  <div class="abs section-label" style="top:92px;font:600 5.4px var(--body);letter-spacing:1.6px">WRITE SOMETHING HERE</div>
  <div class="abs section-label" style="top:98px;font:700 15px var(--head)">Section break</div>
</section>

<!-- 5 One column -->
<section class="slide c2 r2">
  <div class="header-bar">One column text</div>
  <div class="abs copy" style="left:24px;top:58px;width:297px">
    <p>Lorem ipsum dolor sit amet, consectetur adipiscing elit. Donec mauris lorem, vestibulum ac rutrum id, suscipit in dui. Donec vitae dapibus tellus. Vestibulum nunc sem, finibus quis elementum ac, varius ac tellus. Nam faucibus faucibus venenatis. Donec nec arcu velit. Fusce viverra, dui vitae euismod mollis, tortor magna egestas nunc, et suscipit nunc ex quis nunc. Pellentesque habitant morbi tristique senectus et netus et malesuada fames ac turpis egestas. Integer eget auctor nunc. Maecenas tincidunt eleifend consequat. Nulla efficitur urna et massa dapibus maximus. Maecenas sit amet risus pretium, sagittis dui ut, consectetur purus. Phasellus auctor consectetur arcu a consequat. Vestibulum congue sed orci efficitur finibus. Integer malesuada finibus ligula, aliquet lobortis nulla commodo vel.</p>
    <p>Nulla varius vehicula augue, id placerat nisi luctus a. Suspendisse magna tellus, imperdiet id turpis in, gravida fermentum sem. Integer commodo pharetra dui a congue. Vivamus in commodo dui. Nunc fringilla ex sapien, et laoreet erat pretium ultricies. In hac habitasse platea dictumst. Donec lacinia efficitur dictum.</p>
    <p>Cum sociis natoque penatibus et magnis dis parturient montes, nascetur ridiculus mus. Nam odio nulla, tempor a eleifend ut, dignissim nec tellus. Donec porttitor porttitor ante. Nam dictum quam sed erat lobortis, et gravida nunc pellentesque. Mauris gravida ut augue et lobortis.</p>
  </div>
  <span class="page-no">5</span>
</section>

<!-- 6 Two column -->
<section class="slide c3 r2">
  <div class="header-bar">Two column text</div>
  <div class="abs copy" style="left:22px;top:54px;width:141px;font-size:4.3px">
    <p>Lorem ipsum dolor sit amet, consectetur adipiscing elit, sed do eiusmod tempor incididunt ut labore et dolore magna aliqua. Lorem ipsum dolor sit amet, consectetur adipiscing elit, sed do eiusmod tempor incididunt ut labore et dolore magna aliqua. Ut enim ad minim veniam, quis nostrud exercitation ullamco laboris nisi ut aliquip.</p>
    <p>Lorem ipsum dolor sit amet, consectetur adipiscing elit. Lorem ipsum dolor sit amet, consectetur adipiscing elit, sed do eiusmod tempor incididunt ut labore et dolore magna aliqua. Lorem ipsum dolor sit amet eiusmod tempor incididunt ut labore et dolore magna aliqua. Ut enim ad minim veniam, quis nostrud exercitation ullamco laboris nisi ut aliquip, consectetur adipiscing elit, sed do eiusmod tempor incididunt ut labore et dolore magna aliqua. Ut enim ad minim veniam, quis nostrud exercitation ullamco laboris nisi ut aliquip. Eiusmod tempor incididunt ut labore et dolore magna aliqua. Ut enim ad minim veniam, quis nostrud exercitation ullamco laboris nisi ut aliquip.</p>
  </div>
  <div class="abs copy" style="left:178px;top:54px;width:141px;font-size:4.3px">
    <p>Lorem ipsum dolor sit amet, consectetur adipiscing elit, sed do eiusmod tempor incididunt ut labore et dolore magna aliqua. Lorem ipsum dolor sit amet, consectetur adipiscing elit, sed do eiusmod tempor incididunt ut labore et dolore magna aliqua. Ut enim ad minim veniam, quis nostrud exercitation ullamco laboris nisi ut aliquip.</p>
    <p>Lorem ipsum dolor sit amet, consectetur adipiscing elit. Lorem ipsum dolor sit amet, consectetur adipiscing elit, sed do eiusmod tempor incididunt ut labore et dolore magna aliqua. Lorem ipsum dolor sit amet eiusmod tempor incididunt ut labore et dolore magna aliqua. Ut enim ad minim veniam, quis nostrud exercitation ullamco laboris nisi ut aliquip, consectetur adipiscing elit, sed do eiusmod tempor incididunt ut labore et dolore magna aliqua. Ut enim ad minim veniam, quis nostrud exercitation ullamco laboris nisi ut aliquip. Eiusmod tempor incididunt ut labore et dolore magna aliqua. Ut enim ad minim veniam, quis nostrud exercitation ullamco laboris nisi ut aliquip.</p>
  </div>
  <span class="page-no">6</span>
</section>

<!-- 7 Table -->
<section class="slide c1 r3">
  <div class="header-bar" style="padding-left:25px">Table</div>
  <table class="data-table">
    <colgroup><col style="width:77px"><col style="width:56px"><col style="width:55px"><col style="width:56px"><col style="width:55px"></colgroup>
    <tr><th>Example Title</th><th class="alt">Business</th><th>Brand</th><th class="alt">Percent</th><th>Quality</th></tr>
    <tr class="light"><td>Example One</td><td>$40</td><td>$4567</td><td>45%</td><td>$80</td></tr>
    <tr><td>Example Two</td><td>$320</td><td>$356</td><td>60%</td><td>$320</td></tr>
    <tr class="light"><td>Example Three</td><td>$120</td><td>$35</td><td>40%</td><td>$120</td></tr>
    <tr><td>Example Four</td><td>$2</td><td>$3567</td><td>5%</td><td>$2</td></tr>
    <tr class="light"><td>Example Five</td><td>$6730</td><td>$3</td><td>29%</td><td>$6730</td></tr>
    <tr><td>Example Six</td><td>$2</td><td>$3567</td><td>5%</td><td>$2</td></tr>
  </table>
  <span class="page-no">7</span>
</section>

<!-- 8 Vision -->
<section class="slide c2 r3">
  <div class="abs vision-sky" role="img" aria-label="Light city skyline backdrop"></div>
  <div class="abs vision-base"></div>
  <div class="header-bar">Vision, mission, values</div>
  <div class="value-card" style="left:21px">
    <svg width="14" height="13" viewBox="0 0 14 13" aria-hidden="true"><path d="M1,7 L13,1 L9,12 L7,8 Z" fill="#fff"/></svg>
    <h3>MISSION</h3>
    <p>Lorem ipsum dolor sit amet, consectetur adipiscing elit, sed do eiusmod tempor incididunt ut labore et dolore magna aliqua. Lorem ipsum dolor sit amet, consectetur adipiscing elit.</p>
  </div>
  <div class="value-card" style="left:125px">
    <svg width="16" height="13" viewBox="0 0 16 13" aria-hidden="true"><ellipse cx="8" cy="6.5" rx="7.5" ry="4.8" fill="none" stroke="#fff" stroke-width="1.5"/><circle cx="8" cy="6.5" r="2.4" fill="#fff"/></svg>
    <h3>VISION</h3>
    <p>Lorem ipsum dolor sit amet, consectetur adipiscing elit, sed do eiusmod tempor incididunt ut labore et dolore magna aliqua. Lorem ipsum dolor sit amet, consectetur adipiscing elit.</p>
  </div>
  <div class="value-card" style="left:229px">
    <svg width="12" height="14" viewBox="0 0 12 14" aria-hidden="true"><circle cx="6" cy="5" r="4" fill="none" stroke="#fff" stroke-width="1.6"/><path d="M3,8 L2,13 L6,11 L10,13 L9,8" fill="#fff"/></svg>
    <h3>VALUES</h3>
    <p>Lorem ipsum dolor sit amet, consectetur adipiscing elit, sed do eiusmod tempor incididunt ut labore et dolore magna aliqua. Lorem ipsum dolor sit amet, consectetur adipiscing elit.</p>
  </div>
  <span class="page-no">8</span>
</section>

<!-- 10 Growth timeline -->
<section class="slide c3 r3">
  <div class="header-bar" style="padding-left:25px">Lorem ipsum dolor sit amet</div>
  <svg class="abs" width="339" height="191" style="left:0;top:0" aria-hidden="true">
    <polyline points="56,138 131,117 207,97 282,76" fill="none" stroke="#fff" stroke-width="1.6"/>
    <g fill="var(--orange)">
      <circle cx="56" cy="138" r="9.5"/><circle cx="131" cy="117" r="9.5"/>
      <circle cx="207" cy="97" r="9.5"/><circle cx="282" cy="76" r="9.5"/>
    </g>
    <g fill="none" stroke="#fff" stroke-width="1.1">
      <circle cx="56" cy="136" r="2"/><path d="M54.5,138 L53.5,142 L56,140.8 L58.5,142 L57.5,138"/>
      <ellipse cx="131" cy="117" rx="4" ry="2.6"/>
    </g>
    <circle cx="131" cy="117" r="1.3" fill="#fff"/>
    <path d="M203,99 L211,94 L208,101 L207,98 Z" fill="#fff"/>
    <circle cx="280" cy="77" r="2.2" fill="none" stroke="#fff" stroke-width="1.2"/>
    <circle cx="285" cy="74" r="1.6" fill="none" stroke="#fff" stroke-width="1"/>
    <text x="56" y="167" text-anchor="middle" class="milestone" fill="#fff">5M</text>
    <text x="131" y="144" text-anchor="middle" class="milestone" fill="#fff">3M</text>
    <text x="207" y="82" text-anchor="middle" class="milestone" fill="#fff">10M</text>
    <text x="286" y="61" text-anchor="middle" class="milestone" fill="#fff">15M</text>
  </svg>
  <div class="note" style="left:28px;top:73px"><b>Your Text Here</b>Lorem ipsum dolor sit amet, consectetur adipiscing elit, sed do eiusmod tempor incididunt ut labore et dolore magna aliqua.</div>
  <div class="note" style="left:103px;top:55px"><b>Your Text Here</b>Lorem ipsum dolor sit amet, consectetur adipiscing elit, sed do eiusmod tempor incididunt ut labore et dolore magna aliqua.</div>
  <div class="note" style="left:179px;top:123px"><b>Your Text Here</b>Lorem ipsum dolor sit amet, consectetur adipiscing elit, sed do eiusmod tempor incididunt ut labore et dolore magna aliqua.</div>
  <div class="note" style="left:254px;top:108px"><b>Your Text Here</b>Lorem ipsum dolor sit amet, consectetur adipiscing elit, sed do eiusmod tempor incididunt ut labore et dolore magna aliqua.</div>
  <span class="page-no">10</span>
</section>

<!-- Six points -->
<section class="slide c1 r4">
  <div class="header-bar">Six Poins</div>
  <div class="point" style="left:21px;top:51px"><span class="num">01</span><h4>Lorem ipsum dolor sit amet</h4><p>Lorem ipsum dolor sit amet, consectetur adipiscing elit, sed do eiusmod tempor incididunt ut labore et dolore magna aliqua.</p></div>
  <div class="point" style="left:21px;top:86px"><span class="num">02</span><h4>Lorem ipsum dolor sit amet</h4><p>Lorem ipsum dolor sit amet, consectetur adipiscing elit, sed do eiusmod tempor incididunt ut labore et dolore magna aliqua.</p></div>
  <div class="point" style="left:21px;top:119px"><span class="num">03</span><h4>Lorem ipsum dolor sit amet</h4><p>Lorem ipsum dolor sit amet, consectetur adipiscing elit, sed do eiusmod tempor incididunt ut labore et dolore magna aliqua.</p></div>
  <div class="point" style="left:21px;top:154px;border-bottom:0"><span class="num">04</span><h4>Lorem ipsum dolor sit amet</h4><p>Lorem ipsum dolor sit amet, consectetur adipiscing elit, sed do eiusmod tempor incididunt ut labore et dolore magna aliqua.</p></div>
  <div class="point" style="left:179px;top:51px"><span class="num">05</span><h4>Lorem ipsum dolor sit amet</h4><p>Lorem ipsum dolor sit amet, consectetur adipiscing elit, sed do eiusmod tempor incididunt ut labore et dolore magna aliqua.</p></div>
  <div class="point" style="left:179px;top:86px"><span class="num">06</span><h4>Lorem ipsum dolor sit amet</h4><p>Lorem ipsum dolor sit amet, consectetur adipiscing elit, sed do eiusmod tempor incididunt ut labore et dolore magna aliqua.</p></div>
  <div class="point" style="left:179px;top:119px"><span class="num">07</span><h4>Lorem ipsum dolor sit amet</h4><p>Lorem ipsum dolor sit amet, consectetur adipiscing elit, sed do eiusmod tempor incididunt ut labore et dolore magna aliqua.</p></div>
  <div class="point" style="left:179px;top:154px;border-bottom:0"><span class="num">08</span><h4>Lorem ipsum dolor sit amet</h4><p>Lorem ipsum dolor sit amet, consectetur adipiscing elit, sed do eiusmod tempor incididunt ut labore et dolore magna aliqua.</p></div>
  <span class="page-no">6</span>
</section>

<!-- Cycle -->
<section class="slide c2 r4">
  <div class="header-bar" style="padding-left:25px">Lorem ipsum dolor sit amet</div>
  <p class="abs copy" style="left:22px;top:51px;width:131px;font-size:4.3px"><b>Lorem ipsum</b> dolor sit amet, consectetur adipiscing elit. Morbi facilisis tellus sodales rutrum pharetra. Nam fermentum hendrerit sapien, non pharetra justo. Integer luctus ornare lacus nec iaculis. Duis at sapien non est laoreet dapibus. Fusce eu eleifend elit, eu scelerisque sapien. Aenean fringilla velit at imperdiet tempor Curabitur sagittis erat velit.</p>
  <div class="chip" style="left:22px;top:104px"><i><svg width="7" height="9" viewBox="0 0 7 9"><circle cx="3.5" cy="3" r="2.4" fill="none" stroke="#fff" stroke-width="1.1"/><path d="M2,5 L1.4,8.5 L3.5,7.6 L5.6,8.5 L5,5" fill="#fff"/></svg></i>Lorem Ipsum</div>
  <div class="chip" style="left:92px;top:104px"><i><svg width="8" height="8" viewBox="0 0 8 8"><path d="M0.5,4 L7.5,0.5 L5,7.5 L4,4.6 Z" fill="#fff"/></svg></i>Lorem Ipsum</div>
  <div class="chip" style="left:22px;top:130px"><i><svg width="9" height="7" viewBox="0 0 9 7"><ellipse cx="4.5" cy="3.5" rx="4" ry="2.7" fill="none" stroke="#fff" stroke-width="1"/><circle cx="4.5" cy="3.5" r="1.4" fill="#fff"/></svg></i>Lorem Ipsum</div>
  <div class="chip" style="left:92px;top:130px"><i><svg width="7" height="9" viewBox="0 0 7 9"><circle cx="3.5" cy="3" r="2.4" fill="none" stroke="#fff" stroke-width="1.1"/><path d="M2,5 L1.4,8.5 L3.5,7.6 L5.6,8.5 L5,5" fill="#fff"/></svg></i>Lorem Ipsum</div>
  <div class="chip" style="left:22px;top:157px"><i><svg width="8" height="8" viewBox="0 0 8 8"><path d="M0.5,4 L7.5,0.5 L5,7.5 L4,4.6 Z" fill="#fff"/></svg></i>Lorem Ipsum</div>
  <div class="chip" style="left:92px;top:157px"><i><svg width="9" height="7" viewBox="0 0 9 7"><ellipse cx="4.5" cy="3.5" rx="4" ry="2.7" fill="none" stroke="#fff" stroke-width="1"/><circle cx="4.5" cy="3.5" r="1.4" fill="#fff"/></svg></i>Lorem Ipsum</div>
  <svg class="abs" width="339" height="191" style="left:0;top:0" aria-hidden="true">
    <g stroke="#1a69a5" stroke-width="3.5" stroke-linejoin="round">
      <polygon points="243,113 209,54 277,54" fill="#fff"/>
      <polygon points="243,113 277,54 311,113" fill="#2079bb"/>
      <polygon points="243,113 311,113 277,172" fill="#fff"/>
      <polygon points="243,113 277,172 209,172" fill="#2079bb"/>
      <polygon points="243,113 209,172 175,113" fill="#fff"/>
      <polygon points="243,113 175,113 209,54" fill="#2079bb"/>
    </g>
    <circle cx="243" cy="113" r="24" fill="#fff"/>
    <g font-family="Open Sans, sans-serif" font-size="3.8" text-anchor="middle">
      <text fill="#1a69a5"><tspan x="243" y="70">Lorem</tspan><tspan x="243" y="75">ipsum dolor</tspan><tspan x="243" y="80">sit amet</tspan></text>
      <text fill="#fff"><tspan x="283" y="91">Lorem</tspan><tspan x="283" y="96">ipsum dolor</tspan><tspan x="283" y="101">sit amet</tspan></text>
      <text fill="#1a69a5"><tspan x="283" y="129">Lorem</tspan><tspan x="283" y="134">ipsum dolor</tspan><tspan x="283" y="139">sit amet</tspan></text>
      <text fill="#fff"><tspan x="243" y="151">Lorem</tspan><tspan x="243" y="156">ipsum dolor</tspan><tspan x="243" y="161">sit amet</tspan></text>
      <text fill="#1a69a5"><tspan x="203" y="129">Lorem</tspan><tspan x="203" y="134">ipsum dolor</tspan><tspan x="203" y="139">sit amet</tspan></text>
      <text fill="#fff"><tspan x="203" y="91">Lorem</tspan><tspan x="203" y="96">ipsum dolor</tspan><tspan x="203" y="101">sit amet</tspan></text>
      <text fill="#222"><tspan x="243" y="108" font-size="4.8" font-weight="700">Add Text</tspan><tspan x="243" y="114">Easy to change</tspan><tspan x="243" y="118.5">colors, photos and</tspan><tspan x="243" y="123">Text.</tspan></text>
    </g>
  </svg>
  <span class="page-no">10</span>
</section>

<!-- Statistics -->
<section class="slide c3 r4">
  <div class="header-bar" style="padding-left:25px">Statistics</div>
  <div class="abs stat" style="left:23px;top:79px">50 %</div>
  <div class="abs stat" style="left:23px;top:132px">20 %</div>
  <svg class="abs" width="339" height="191" style="left:0;top:0" aria-hidden="true">
    <defs>
      <g id="person">
        <circle cx="4" cy="1.8" r="1.8"/>
        <path d="M1,4.5 H7 Q8,4.5 8,5.5 V11 H6.8 V19 H5 V12 H3 V19 H1.2 V11 H0 V5.5 Q0,4.5 1,4.5 Z"/>
      </g>
    </defs>
    <g fill="#fff">
      <use href="#person" x="66" y="78"/><use href="#person" x="76.7" y="78"/><use href="#person" x="87.4" y="78"/><use href="#person" x="98.1" y="78"/><use href="#person" x="108.8" y="78"/>
    </g>
    <g fill="var(--orange)">
      <use href="#person" x="119.5" y="78"/><use href="#person" x="130.2" y="78"/><use href="#person" x="140.9" y="78"/><use href="#person" x="151.6" y="78"/><use href="#person" x="162.3" y="78"/>
    </g>
    <g fill="#fff">
      <use href="#person" x="66" y="131"/><use href="#person" x="76.7" y="131"/><use href="#person" x="87.4" y="131"/><use href="#person" x="98.1" y="131"/><use href="#person" x="108.8" y="131"/><use href="#person" x="119.5" y="131"/><use href="#person" x="130.2" y="131"/><use href="#person" x="140.9" y="131"/>
    </g>
    <g fill="var(--orange)">
      <use href="#person" x="151.6" y="131"/><use href="#person" x="162.3" y="131"/>
    </g>
    <g stroke="#fff" stroke-width=".5">
      <line x1="207" y1="57" x2="207" y2="154"/>
      <line x1="207" y1="154" x2="320" y2="154"/>
    </g>
    <g font-family="Open Sans, sans-serif" font-size="4.2" fill="#fff" text-anchor="end">
      <text x="202" y="59">60</text><text x="202" y="75">50</text><text x="202" y="91">40</text><text x="202" y="108">30</text><text x="202" y="124">20</text><text x="202" y="140">10</text><text x="202" y="156">0</text>
    </g>
    <g font-family="Open Sans, sans-serif" font-size="4.2" fill="#fff" text-anchor="middle">
      <text x="223" y="162">Text 1</text><text x="250" y="162">Text 2</text><text x="277" y="162">Text 3</text><text x="304" y="162">Text 4</text>
    </g>
    <polyline points="223,116 250,84 277,125 304,73" fill="none" stroke="#fff" stroke-width=".9"/>
    <g fill="#fff"><circle cx="223" cy="116" r="1"/><circle cx="250" cy="84" r="1"/><circle cx="277" cy="125" r="1"/><circle cx="304" cy="73" r="1"/></g>
  </svg>
  <span class="page-no">12</span>
</section>

</body>
</html>
```